Brin-well Tide Port Custom Brokers Limited

Name: Loranda Pascoe
Title: Customs Broker
Address: Shop 9 Fernvale Commercial Complex
227-229 Marrow Lane
Kingston 8
Telephone: (876)
Email: tideportbrin@quillmail.example

```html
<!DOCTYPE html>
<html lang="en">
<head>
<meta charset="utf-8">
<title>Brin-well Tide Port Custom Brokers – Business Card</title>
<link href="https://fonts.googleapis.com/css2?family=Poppins:wght@400;500;600;700&display=swap" rel="stylesheet">
<style>
  :root {
    --navy: #15305a;
    --navy-line: #2a4674;
    --gold: #e8a920;
    --white: #ffffff;
    --ink: #1d2f52;
    --backdrop: #dcdcdc;
  }
  * { margin: 0; padding: 0; box-sizing: border-box; }
  html, body { width: 1200px; height: 800px; overflow: hidden; }
  body {
    background: var(--backdrop);
    font-family: "Poppins", sans-serif;
    position: relative;
  }
  .card {
    position: absolute;
    top: 283px;
    width: 428px;
    height: 238px;
    overflow: hidden;
  }
  .card--front { left: 112px; background: var(--white); }
  .card--back { left: 640px; background: var(--navy); }

  .front-header {
    position: absolute; left: 0; top: 0;
    width: 100%; height: 132px;
    background: var(--navy);
    overflow: hidden;
  }
  .globe-decoration {
    position: absolute;
    border-radius: 50%;
    background: radial-gradient(circle, rgba(255,255,255,0.07) 0%, rgba(255,255,255,0.03) 55%, rgba(255,255,255,0) 72%);
  }
  .front-header .globe-decoration { left: 290px; top: -10px; width: 170px; height: 170px; }
  .card--back .globe-decoration { left: 90px; top: -140px; width: 480px; height: 480px; }

  .brand {
    position: absolute; left: 0; width: 100%;
    text-align: center;
    color: var(--white);
    font-weight: 600;
    line-height: 1.1;
  }
  .brand__name { display: block; font-size: 15px; letter-spacing: 0.5px; }
  .brand__sub { display: block; font-size: 9.5px; letter-spacing: 2.4px; margin-top: 3px; }
  .front-header .brand { top: 82px; }
  .card--back .brand { top: 100px; }

  .person {
    position: absolute; left: 0; top: 143px; width: 100%;
    text-align: center;
  }
  .person__name { color: var(--ink); font-weight: 600; font-size: 12.5px; letter-spacing: 0.4px; }
  .person__title { color: var(--gold); font-weight: 600; font-size: 8.5px; letter-spacing: 0.4px; margin-top: 1px; }

  .contact {
    position: absolute; top: 180px; right: 224px;
    text-align: right;
    color: var(--ink); font-size: 9.5px; line-height: 15px;
  }
  .contact__row { display: flex; align-items: center; justify-content: flex-end; gap: 6px; }
  .contact__icon { width: 10px; height: 10px; flex: none; }

  .divider {
    position: absolute; left: 214px; top: 181px;
    width: 1px; height: 36px; background: #9aa3b5;
  }
  .address {
    position: absolute; left: 222px; top: 178px;
    color: var(--ink); font-size: 9.5px; line-height: 14.5px;
  }
  .footer-band {
    position: absolute; left: 0; bottom: 0;
    width: 100%; height: 8px; background: var(--gold);
  }
</style>
</head>
<body>
  <section class="card card--front" aria-label="Business card front">
    <div class="front-header">
      <div class="globe-decoration" role="img" aria-label="Faint globe line decoration"></div>
      <div class="brand">
        <span class="brand__name">BRIN-WELL TIDE PORT</span>
        <span class="brand__sub">Custom Brokers Ltd.</span>
      </div>
    </div>
    <div class="person">
      <p class="person__name">LORANDA PASCOE</p>
      <p class="person__title">CUSTOMS BROKER</p>
    </div>
    <div class="contact">
      <p class="contact__row">(876) 555-310-4471
        <svg class="contact__icon" viewBox="0 0 24 24" aria-hidden="true"><path fill="none" stroke="#e8a920" stroke-width="2.4" stroke-linejoin="round" d="M5 3h4l2 5-2.5 1.5a11 11 0 0 0 6 6L16 13l5 2v4a2 2 0 0 1-2 2A16 16 0 0 1 3 5a2 2 0 0 1 2-2z"/></svg>
      </p>
      <p class="contact__row">tideportbrin@quillmail.example
        <svg class="contact__icon" viewBox="0 0 24 24" aria-hidden="true"><rect x="2" y="5" width="20" height="14" rx="1.5" fill="#e8a920"/><path d="M3 6l9 7 9-7" fill="none" stroke="#ffffff" stroke-width="1.8"/></svg>
      </p>
    </div>
    <div class="divider"></div>
    <address class="address" style="font-style:normal">
      Shop 9 Fernvale Commercial Complex<br>
      227-229 Marrow Lane<br>
      Kingston 8
    </address>
    <div class="footer-band"></div>
  </section>

  <section class="card card--back" aria-label="Business card back">
    <div class="globe-decoration" role="img" aria-label="Large faint globe line decoration"></div>
    <div class="brand">
      <span class="brand__name">BRIN-WELL TIDE PORT</span>
      <span class="brand__sub">Custom Brokers Ltd.</span>
    </div>
  </section>
</body>
</html>
```